Bref créative
Business cards, invoice, letterhead
Stationery for baby immunisation service
Professional
Thandeka Zulani
Dr
42 9th Avenue
Brenthill
Johannesburg
drtzulani@kovahealth.co.za
PR 0738261

```html
<!DOCTYPE html>
<html lang="en">
<head>
<meta charset="utf-8">
<title>Tiny Sprouts – Business Card</title>
<link href="https://fonts.googleapis.com/css2?family=Open+Sans:ital,wght@0,400;0,600;0,700;1,400&display=swap" rel="stylesheet">
<style>
  :root {
    --stage: #ececea;
    --card-white: #ffffff;
    --rose: #ec5d73;
    --rose-deep: #e24d66;
    --rose-soft: #f28a9b;
    --leaf: #7cb342;
    --teal: #2aa8b8;
    --ink: #555a60;
    --rule: #c9c9c9;
  }
  * { box-sizing: border-box; margin: 0; padding: 0; }
  html, body { width: 1200px; height: 402px; overflow: hidden; }
  body {
    background: var(--stage);
    font-family: "Open Sans", Arial, sans-serif;
    color: var(--ink);
    position: relative;
  }
  .card {
    position: absolute;
    top: 42px;
    width: 560px;
    height: 318px;
    box-shadow: 0 6px 14px rgba(0,0,0,.18);
    overflow: hidden;
  }
  .card--front { left: 30px; background: var(--card-white); }
  .card--back { left: 610px; background: var(--rose); }

  .front-band {
    position: absolute; left: 0; right: 0; bottom: 0; height: 14px;
    background: var(--rose);
  }
  .front-accent {
    position: absolute; left: 0; bottom: 14px; width: 250px; height: 3px;
    background: var(--teal);
  }

  .brand {
    position: absolute; left: 24px; top: 70px; width: 240px; text-align: center;
  }
  .brand__mark {
    width: 58px; height: 58px; border-radius: 50%;
    background: var(--rose-soft); margin: 0 auto 12px;
  }
  .brand__name {
    font-size: 34px; font-weight: 600; color: var(--leaf); letter-spacing: -.5px;
    line-height: 1;
  }
  .brand__tagline {
    margin-top: 6px; font-size: 12px; font-style: italic; color: var(--teal);
  }

  .address {
    position: absolute; left: 24px; top: 218px; width: 230px;
    text-align: right; font-size: 11.5px; line-height: 1.6;
  }

  .divider {
    position: absolute; left: 272px; top: 170px; width: 1px; height: 110px;
    background: var(--rule);
  }

  .contact { position: absolute; left: 292px; top: 178px; width: 250px; }
  .contact__name {
    font-size: 14px; font-weight: 700; color: var(--rose-deep);
    padding-bottom: 6px; border-bottom: 1px solid var(--rule); margin-bottom: 10px;
  }
  .contact__row {
    display: flex; align-items: center; gap: 8px;
    font-size: 11.5px; line-height: 1; margin-bottom: 9px;
  }
  .contact__icon { width: 12px; height: 12px; flex: none; }

  .back-art {
    position: absolute; inset: 0;
  }
</style>
</head>
<body>
  <section class="card card--front" aria-label="Business card front">
    <div class="brand">
      <div class="brand__mark"></div>
      <div class="brand__name">Tiny Sprouts</div>
      <div class="brand__tagline">infancy to early childhood</div>
    </div>

    <address class="address" style="font-style:normal">
      42 9th Avenue<br>
      Brenthill, Johannesburg<br>
      License No. PR 0738261
    </address>

    <div class="divider"></div>

    <div class="contact">
      <div class="contact__name">Dr. Thandeka Zulani</div>
      <div class="contact__row">
        <svg class="contact__icon" viewBox="0 0 12 12"><circle cx="6" cy="6" r="6" fill="#2aa8b8"/><path d="M3.8 3.2l1 .1.5 1.4-.7.5a4 4 0 0 0 2 2l.5-.7 1.4.5.1 1c-2.5.6-5.4-2.3-4.8-4.8z" fill="#fff"/></svg>
        <span>+27 11 555 0142</span>
      </div>
      <div class="contact__row">
        <svg class="contact__icon" viewBox="0 0 12 12"><rect x="3" y="0.5" width="6" height="11" rx="1.2" fill="#2aa8b8"/><rect x="4" y="2" width="4" height="6.5" fill="#fff"/></svg>
        <span>+27 82 555 0718</span>
      </div>
      <div class="contact__row">
        <svg class="contact__icon" viewBox="0 0 12 12"><rect x="0.5" y="2.5" width="11" height="7.5" rx="1" fill="#2aa8b8"/><path d="M1 3l5 4 5-4" fill="none" stroke="#fff" stroke-width="1"/></svg>
        <span>drtzulani@kovahealth.co.za</span>
      </div>
    </div>

    <div class="front-accent"></div>
    <div class="front-band"></div>
  </section>

  <section class="card card--back" aria-label="Business card back">
    <svg class="back-art" viewBox="0 0 560 318" role="img" aria-label="Line illustration of a mother holding her baby, with a faint larger echo of the brand emblem behind">
      <defs>
        <radialGradient id="back-glow-left" cx="0.5" cy="0.5" r="0.5">
          <stop offset="0" stop-color="#f4a0ad" stop-opacity=".45"/>
          <stop offset="1" stop-color="#ec5d73" stop-opacity="0"/>
        </radialGradient>
        <radialGradient id="back-glow-right" cx="0.5" cy="0.5" r="0.5">
          <stop offset="0" stop-color="#fbd3d9" stop-opacity=".55"/>
          <stop offset="1" stop-color="#ec5d73" stop-opacity="0"/>
        </radialGradient>
      </defs>
      <ellipse cx="190" cy="170" rx="150" ry="140" fill="url(#back-glow-left)"/>
      <ellipse cx="420" cy="170" rx="130" ry="150" fill="url(#back-glow-right)"/>
    </svg>
  </section>
</body>
</html>
```